iOS7 test prep app

I need 3 basic screens and 2 product images for an iOS7 app I am prototyping. I provided lots of detail in the attached brief. This is an education product, so warm colors (especially reds) work best.

If you've done flat design for mobile products, please take a look ... Thanks!

Greetings, all. Thank you for your submissions. I am meeting with my product development team this week to review your submissions, and will select a designer before the end of the week. I appreciate your patience with my process, and thank you again for your interest in my project. I'll be back to you soon ... -Gordon

```html
<!DOCTYPE html>
<html lang="en">
<head>
<meta charset="utf-8">
<title>Quiz App Screens</title>
<link rel="stylesheet" href="https://fonts.googleapis.com/css2?family=Open+Sans:wght@400;600;700&display=swap">
<style>
  :root {
    --page-bg: #f4f4f2;
    --screen-bg: #ebebeb;
    --card-bg: #ffffff;
    --brand-red: #d42426;
    --brand-green: #46a928;
    --correct-bg: #c4ee6b;
    --text-main: #3a3a3a;
    --text-body: #4a4a4a;
    --wrong-icon: #c8242a;
    --track: #d6d6d6;
    --border: #dcdcdc;
  }
  * { box-sizing: border-box; margin: 0; padding: 0; }
  html, body {
    width: 1091px; height: 1200px; overflow: hidden;
    background: var(--page-bg);
    font-family: "Open Sans", Arial, sans-serif;
  }
  .stage {
    position: relative; width: 1003px; height: 1103px;
    transform: scale(1.0877); transform-origin: 0 0;
  }
  .screen {
    position: absolute; top: 180px; width: 371px; height: 748px;
    background: var(--screen-bg); overflow: hidden;
    box-shadow: 0 2px 10px rgba(0,0,0,.15);
  }
  .screen--ask { left: 66px; }
  .screen--answer { left: 566px; }
  .app-bar {
    position: absolute; left: 0; top: 0; width: 100%; height: 50px;
    background: var(--brand-red); color: #fff;
    display: flex; align-items: center; justify-content: center;
    font-weight: 700; font-size: 15px; letter-spacing: .1px;
  }
  .menu-icon { position: absolute; left: 22px; top: 17px; }
  .help-icon { position: absolute; left: 20px; top: 152px; }
  .question-card {
    position: absolute; left: 65px; top: 75px; width: 286px; height: 187px;
    background: var(--card-bg); padding: 18px 10px 0 20px;
    font-size: 14.6px; line-height: 26px; color: var(--text-body);
  }
  .option {
    position: absolute; left: 21px; width: 330px; height: 45px;
    background: var(--card-bg); border-bottom: 1px solid var(--border);
    display: flex; align-items: center; padding-left: 18px;
    font-weight: 700; font-size: 14.6px; color: var(--text-main);
  }
  .option .letter { margin-right: 8px; }
  .option--correct { background: var(--correct-bg); }
  .option .mark { position: absolute; right: 11px; top: 12px; }
  .btn {
    position: absolute; height: 46px; color: #fff;
    display: flex; align-items: center; justify-content: center;
    font-weight: 700; font-size: 15.5px;
  }
  .btn--red { background: var(--brand-red); }
  .btn--green { background: var(--brand-green); }
  .slider { position: absolute; left: 24px; top: 606px; }
  .explanation {
    position: absolute; left: 21px; top: 512px; width: 330px; height: 142px;
    background: var(--card-bg); padding: 15px 20px 0 21px;
    font-size: 14px; line-height: 23px; color: var(--text-main);
  }
  .explanation strong { font-weight: 700; }
</style>
</head>
<body>
<div class="stage">
  <svg width="0" height="0" style="position:absolute">
    <defs>
      <g id="wrong-mark"><circle cx="10" cy="10" r="8.5" fill="none" stroke="#c8242a" stroke-width="2"/><path d="M7 7l6 6M13 7l-6 6" stroke="#c8242a" stroke-width="2" stroke-linecap="round"/></g>
      <g id="right-mark"><circle cx="10" cy="10" r="8.5" fill="none" stroke="#3f6b2a" stroke-width="1.6"/><path d="M6 10.5l3 3 5-6" fill="none" stroke="#3f6b2a" stroke-width="1.8" stroke-linecap="round" stroke-linejoin="round"/></g>
      <g id="menu"><rect width="30" height="3" fill="#fff"/><rect y="6" width="30" height="3" fill="#fff"/><rect y="12" width="30" height="3" fill="#fff"/></g>
      <g id="help">
        <circle cx="17" cy="17" r="16" fill="#1e8fbf"/>
        <circle cx="17" cy="17" r="14" fill="#2ea6d6"/>
        <text x="17" y="25" text-anchor="middle" font-family="Open Sans, Arial, sans-serif" font-weight="700" font-size="22" fill="#fff">?</text>
      </g>
    </defs>
  </svg>

  <!-- Question screen -->
  <section class="screen screen--ask">
    <header class="app-bar">
      <svg class="menu-icon" width="30" height="15"><use href="#menu"/></svg>
      QUESTION 7 OF 100
    </header>
    <svg class="help-icon" width="34" height="34"><use href="#help"/></svg>
    <p class="question-card">A patient presents to the emergency room with the following symptoms: Anxiety, dyspnea, rhonchi, fever, Oxygen saturation of 88%, and a pH of 7.21. The nurse realized that the patient suffering from:</p>
    <div class="option" style="top:277px"><span class="letter">A.</span>RESPIRATORY ALKALOSIS</div>
    <div class="option" style="top:335px"><span class="letter">B.</span>METABOLIC ALKALOSIS</div>
    <div class="option" style="top:394px"><span class="letter">C.</span>RESPIRATORY ACIDOSIS</div>
    <div class="option" style="top:453px"><span class="letter">D.</span>METABOLIC ACIDOSIS</div>
    <div class="btn btn--red" style="left:107px;top:525px;width:156px;">CONFIDENCE</div>
    <svg class="slider" width="326" height="44" viewBox="0 0 326 44">
      <defs>
        <linearGradient id="fill" x1="0" x2="1"><stop offset="0" stop-color="#e8260e"/><stop offset="1" stop-color="#ff6a10"/></linearGradient>
      </defs>
      <circle cx="17" cy="22" r="17" fill="#e2e2e2"/>
      <circle cx="17" cy="22" r="13" fill="#d6231d"/>
      <rect x="11" y="21" width="12" height="2.4" fill="#fff"/>
      <rect x="53" y="17.5" width="219" height="9" rx="4.5" fill="var(--track)"/>
      <rect x="53" y="17.5" width="142" height="9" rx="4.5" fill="url(#fill)"/>
      <circle cx="194" cy="22" r="11" fill="#f3f3f3" stroke="#cfcfcf"/>
      <circle cx="194" cy="22" r="3.5" fill="#d8d8d8"/>
      <circle cx="306" cy="22" r="17" fill="#e2e2e2"/>
      <circle cx="306" cy="22" r="13" fill="#3da12a"/>
      <rect x="300" y="20.8" width="12" height="2.4" fill="#fff"/>
      <rect x="304.8" y="16" width="2.4" height="12" fill="#fff"/>
    </svg>
    <div class="btn btn--green" style="left:107px;top:676px;width:156px;">SUBMIT</div>
  </section>

  <!-- Answer screen -->
  <section class="screen screen--answer">
    <header class="app-bar">
      <svg class="menu-icon" width="30" height="15"><use href="#menu"/></svg>
      QUESTION 7 OF 100
    </header>
    <svg class="help-icon" width="34" height="34"><use href="#help"/></svg>
    <p class="question-card">A patient presents to the emergency room with the following symptoms: Anxiety, dyspnea, rhonchi, fever, Oxygen saturation of 88%, and a pH of 7.21. The nurse realized that the patient suffering from:</p>
    <div class="option" style="top:277px"><span class="letter">A.</span>RESPIRATORY ALKALOSIS<svg class="mark" width="20" height="20"><use href="#wrong-mark"/></svg></div>
    <div class="option" style="top:335px"><span class="letter">B.</span>METABOLIC ALKALOSIS<svg class="mark" width="20" height="20"><use href="#wrong-mark"/></svg></div>
    <div class="option option--correct" style="top:394px"><span class="letter">C.</span>RESPIRATORY ACIDOSIS<svg class="mark" width="20" height="20"><use href="#right-mark"/></svg></div>
    <div class="option" style="top:453px"><span class="letter">D.</span>METABOLIC ACIDOSIS<svg class="mark" width="20" height="20"><use href="#wrong-mark"/></svg></div>
    <p class="explanation"><strong>The correct answer is C.</strong> A key symptom of respiratory distress syndrome is the inability of the respiratory system to exchange gases, resulting in respiratory. acidosis.</p>
    <div class="btn btn--red" style="left:21px;top:676px;width:156px;">SAVE &amp; CLOSE</div>
    <div class="btn btn--green" style="left:196px;top:676px;width:155px;">NEXT QUESTION</div>
  </section>
</div>
</body>
</html>
```